High End Business Card Design for Flooring Store

Looking for a new card design for our hardwood flooring company. We have no print budget for these and are open to cards made from wood, metal, cardstock with embossed print ... or any combination of these. No plastic.

We sell luxury products and I want the cards to reflect our image of quality and class.

Our contact information as such;
Employee Name
418 Colbrook Blvd.
Maplewood, ON
K9R-3M5
(555) 214-3968
Employee email @velkaflooring.com

Target Market(s)

Home Builders

Contact Information for Business Card

Emnployee name, business contact information

```html
<!DOCTYPE html>
<html lang="en">
<head>
<meta charset="utf-8">
<title>Velka Flooring – Business Card</title>
<link rel="stylesheet" href="https://fonts.googleapis.com/css2?family=Montserrat:wght@400;500;700&display=swap">
<style>
  :root {
    --page-bg: #e4ddd2;
    --ink: #33180e;
    --ink-soft: rgba(51,24,14,0.85);
    --wood-light: #c8946a;
    --wood-mid: #a8704a;
    --wood-dark: #6e4128;
  }
  * { box-sizing: border-box; margin: 0; padding: 0; }
  html, body {
    width: 1200px; height: 1008px; overflow: hidden;
    background: var(--page-bg);
  }
  .card {
    position: absolute; left: 75px; top: 204px;
    width: 1050px; height: 600px; overflow: hidden;
    font-family: "Montserrat", sans-serif; color: var(--ink);
  }
  .wood-grain {
    position: absolute; inset: 0;
    background:
      linear-gradient(160deg, transparent 30%, rgba(110,65,40,.35) 45%, transparent 58%),
      linear-gradient(175deg, var(--wood-mid) 0%, var(--wood-light) 35%, var(--wood-mid) 60%, var(--wood-light) 85%, var(--wood-mid) 100%);
  }
  .feature-graphic {
    position: absolute; left: 600px; top: 40px;
    width: 450px; height: 520px;
    background: linear-gradient(90deg, rgba(51,24,14,0) 0%, rgba(51,24,14,.55) 40%, var(--ink-soft) 100%);
  }
  .brand {
    position: absolute; left: 92px; top: 66px;
    display: flex; align-items: center; gap: 22px;
  }
  .brand-mark { width: 44px; height: 44px; background: var(--ink); }
  .brand-name { font-size: 118px; font-weight: 400; line-height: 1; letter-spacing: 1px; }
  .tagline {
    position: absolute; left: 158px; top: 196px;
    font-size: 26px; font-weight: 500; line-height: 1.15;
  }
  .rule { position: absolute; height: 2px; background: var(--ink); }
  .rule-top { left: 158px; top: 186px; width: 360px; }
  .rule-bottom { left: 158px; top: 272px; width: 250px; }
  .employee {
    position: absolute; left: 158px; top: 296px;
    font-size: 34px; font-weight: 700; letter-spacing: 2px;
  }
  .contact { position: absolute; left: 158px; display: flex; align-items: flex-start; gap: 20px; }
  .contact svg { flex: none; width: 30px; height: 30px; fill: var(--ink); margin-top: 6px; }
  .address { top: 356px; font-size: 32px; line-height: 1.1; }
  .phone { top: 474px; font-size: 38px; font-weight: 700; letter-spacing: 1px; }
  .email { top: 534px; font-size: 36px; }
</style>
</head>
<body>
  <main class="card">
    <div class="wood-grain" role="img" aria-label="Warm walnut wood grain surface"></div>
    <div class="feature-graphic" role="img" aria-label="Dark brown decorative graphic area"></div>

    <div class="brand">
      <span class="brand-mark"></span>
      <span class="brand-name">Velka</span>
    </div>
    <div class="rule rule-top"></div>
    <p class="tagline">Planchers &amp; Escaliers<br>Flooring &amp; Stairs</p>
    <div class="rule rule-bottom"></div>

    <p class="employee">ALEX MORIN</p>

    <div class="contact address">
      <svg viewBox="0 0 24 24"><path d="M12 2a7 7 0 0 0-7 7c0 5 7 13 7 13s7-8 7-13a7 7 0 0 0-7-7zm0 9.5A2.5 2.5 0 1 1 12 6.5a2.5 2.5 0 0 1 0 5z"/></svg>
      <p>418 Colbrook Blvd.<br>Maplewood, ON<br>K9R-3M5</p>
    </div>

    <div class="contact phone">
      <svg viewBox="0 0 24 24"><path d="M6.6 10.8a15 15 0 0 0 6.6 6.6l2.2-2.2a1 1 0 0 1 1-.25 11.4 11.4 0 0 0 3.6.57 1 1 0 0 1 1 1V20a1 1 0 0 1-1 1A17 17 0 0 1 3 4a1 1 0 0 1 1-1h3.5a1 1 0 0 1 1 1c0 1.250.2 2.450.57 3.57a1 1 0 0 1-.25 1z"/></svg>
      <p>(555) 214-3968</p>
    </div>

    <div class="contact email">
      <svg viewBox="0 0 24 24"><path d="M2 5h20v14H2zm2 2v.5l8 5 8-5V7l-8 5z"/></svg>
      <p>email@velkaflooring.com</p>
    </div>
  </main>
</body>
</html>
```